Golf Lesson Monthly Subscription Flyer

I need a flyer design for a monthly subscription golf lesson package. What's different about this package is that it includes live lessons, online lessons used for check ins, and a monthly subscription to my video paysite. I have 3 different tiers with different options in each tier. I need an easy to read flyer that I can email to my email list.

Target Market(s)

Golfers with excess money for lessons. Usually 50+ age

Colors

Designer to choose colors to be used in the design.

Requirements
Must have
• Needs to say "Cedar Hollow Coaching School" with the logo somewhere on the flyer.
• Also dale-pemberton.example needs to be on the flyer.

```html
<!DOCTYPE html>
<html lang="en">
<head>
<meta charset="utf-8">
<title>Dale Pemberton Golf Flyer Design</title>
<link rel="stylesheet" href="https://fonts.googleapis.com/css2?family=Oswald:wght@400;500;600;700&family=Poppins:wght@400;500;700&family=Montserrat:wght@500&display=swap">
<style>
:root{
  --board-dark:#2f2f2f;
  --board-mid:#4d4d4d;
  --red:#e4232b;
  --coral:#ee6a55;
  --ink:#1c1c1c;
  --brush:#333333;
  --tier-gray:#e2e3e5;
  --teal:#53b8c5;
  --yellow:#ffe600;
  --white:#ffffff;
}
*{margin:0;padding:0;box-sizing:border-box}
html,body{width:1200px;height:1029px;overflow:hidden}
body{
  background:radial-gradient(ellipse at 50% 45%,var(--board-mid),var(--board-dark) 75%);
  font-family:"Poppins",sans-serif;color:var(--white);position:relative;
}
.board-title{position:absolute;top:44px;left:0;width:1200px;text-align:center;
  font-family:"Montserrat",sans-serif;font-weight:500;font-size:26px;letter-spacing:.5px}
.side-label{position:absolute;top:193px;width:541px;text-align:center;
  font-family:"Montserrat",sans-serif;font-weight:500;font-size:20px}
.side-label.front{left:51px}
.side-label.back{left:620px}

.flyer{position:absolute;top:247px;width:541px;height:701px;overflow:hidden;
  box-shadow:0 6px 22px rgba(0,0,0,.45)}
.flyer.front{left:51px;background:linear-gradient(180deg,#fafafa,#ececec)}
.flyer.back{left:620px;background:radial-gradient(ellipse at 50% 40%,#ffffff,#e9e9e9 80%)}
.flyer svg.shapes{position:absolute;left:0;top:0}
.abs{position:absolute}
.center{left:0;width:541px;text-align:center}

.wordmark{position:absolute;font-family:"Poppins",sans-serif;font-weight:400;line-height:.95;text-transform:uppercase}
.front .wordmark{left:62px;top:28px;color:var(--white);font-size:19px}
.back .wordmark{left:66px;top:42px;color:var(--ink);font-size:20px}
.mark-dot{position:absolute;border-radius:50%}
.front .mark-dot{left:24px;top:40px;width:26px;height:26px;background:var(--white)}
.back .mark-dot{left:26px;top:52px;width:28px;height:28px;background:var(--red)}

.academy{top:366px;font-family:"Oswald",sans-serif;font-weight:700;font-size:36px;color:var(--red);letter-spacing:.3px}
.credentials{top:412px;font-size:12.6px;line-height:20px;color:var(--ink)}
.credentials b{font-weight:700}
.brush-title{font-family:"Oswald",sans-serif;font-weight:600;color:var(--white);text-align:center;letter-spacing:.4px}
.front .brush-title{left:110px;width:330px;top:478px;font-size:22px}
.service{top:529px;font-size:12.2px;line-height:18.2px;color:var(--ink)}
.service b{font-weight:700}
.web{top:652px;font-family:"Poppins",sans-serif;font-weight:700;font-size:22px;color:var(--white);
  display:flex;justify-content:center;align-items:center;gap:12px;height:42px}
.web .rule{width:48px;height:2px;background:var(--white)}

.back .brush-title{left:208px;width:310px;top:48px;font-size:19.5px;line-height:23px}
.tier{font-family:"Oswald",sans-serif;color:var(--white);text-align:center;left:0;width:541px}
.tier .name{font-weight:500;font-size:13px;line-height:16px}
.tier .lines{font-weight:400;font-size:7px;line-height:9.2px}
.tier .pack{font-weight:400;font-size:10px;line-height:12px}
.tier em{font-style:normal;color:var(--yellow)}
.tier.two{color:var(--ink)}
.tier.two em{color:var(--red)}
.tier.two .lines{font-size:7.4px;line-height:10.2px}
.tier.two .pack{font-size:10.8px;line-height:11.8px}
.tier.three .lines{font-size:7.4px;line-height:10.4px}
.tier.three .pack{font-size:10.8px;line-height:11.8px}
.payments{top:561px;font-size:18.5px;line-height:20px;color:var(--ink)}
.payments span{color:var(--red)}
.contact{left:28px;top:621px;width:258px;font-size:12.4px;line-height:14px;color:var(--white);white-space:nowrap}
.contact .label{color:var(--yellow);font-weight:700}
.contact .head{color:var(--yellow);font-size:14px;font-weight:500}
.badge{position:absolute;top:625px;width:68px;height:68px;border-radius:50%}
.badge.one{left:293px;background:#1f1f1f;border:3px solid var(--white)}
.badge.two{left:370px;background:#23325e;border:3px solid var(--white)}
.badge.three{left:449px;background:var(--white)}
</style>
</head>
<body>

<h1 class="board-title">DALE PEMBERTON GOLF FLYER DESIGN</h1>
<p class="side-label front">FRONT SIDE</p>
<p class="side-label back">BACK SIDE</p>

<section class="flyer front">
  <svg class="shapes" width="541" height="701" viewBox="0 0 541 701">
    <defs>
      <linearGradient id="scene" x1="0" y1="0" x2="0" y2="1">
        <stop offset="0" stop-color="#9cc7ea"/>
        <stop offset=".42" stop-color="#c7ddee"/>
        <stop offset=".55" stop-color="#5d7a3c"/>
        <stop offset="1" stop-color="#7fa04a"/>
      </linearGradient>
      <linearGradient id="grass" x1="0" y1="0" x2="0" y2="1">
        <stop offset="0" stop-color="#8fd14a"/>
        <stop offset="1" stop-color="#4f9c23"/>
      </linearGradient>
      <radialGradient id="ball" cx=".4" cy=".35" r=".7">
        <stop offset="0" stop-color="#ffffff"/>
        <stop offset="1" stop-color="#cfcfcf"/>
      </radialGradient>
    </defs>
    <path role="img" aria-label="Photo of a golfer in a red shirt finishing his drive on a sunny fairway"
      fill="url(#scene)" d="M0,0 H541 V187 C470,190 420,230 380,280 C340,330 300,352 262,348 C215,343 180,300 140,255 C100,212 50,195 0,193 Z"/>
    <path fill="var(--red)" d="M0,188 C55,190 105,212 145,255 C185,300 218,346 262,350 C300,353 340,330 380,282 C420,232 470,190 541,182 V205 C475,212 425,252 390,300 C350,350 305,372 262,370 C215,368 180,330 140,285 C100,242 50,235 0,240 Z"/>
    <path fill="var(--coral)" opacity=".85" d="M0,238 C50,233 100,240 140,285 C180,330 215,366 262,368 C305,370 350,348 390,298 C425,250 475,210 541,203 V215 C480,222 430,262 395,308 C355,358 305,380 262,378 C210,376 175,340 135,295 C95,252 50,246 0,250 Z"/>
    <path fill="#c9dff0" d="M0,0 H280 C240,18 215,65 165,100 C115,130 45,126 0,92 Z"/>
    <path fill="var(--red)" d="M0,0 H265 C225,20 205,62 155,94 C105,122 40,116 0,84 Z"/>
    <rect x="23" y="588" width="6" height="56" fill="var(--red)"/>
    <circle role="img" aria-label="Golf ball resting on a red tee" cx="20" cy="570" r="21" fill="url(#ball)"/>
    <rect role="img" aria-label="Strip of green grass" x="0" y="627" width="541" height="23" fill="url(#grass)"/>
    <rect x="0" y="649" width="541" height="52" fill="var(--red)"/>
    <path fill="var(--brush)" d="M114,474 L160,468 L300,466 L438,470 L436,478 L420,481 L430,490 L438,495 L408,500 L434,506 L410,512 L380,518 L250,521 L150,519 L124,512 L132,506 L110,500 L124,494 L112,486 L126,482 Z"/>
  </svg>

  <span class="mark-dot"></span>
  <div class="wordmark">Dale<br>Pemberton<br>Golf</div>

  <h2 class="abs center academy">CEDAR HOLLOW COACHING SCHOOL</h2>
  <p class="abs center credentials">Dale’s credentials are Fairway Monthly Top Teachers in State List<br><b>2017-2018</b> and <b>2016</b> Utah Section Pro Guild Teacher of the Year</p>
  <h3 class="abs brush-title">DESCRIPTION OF SERVICE</h3>
  <p class="abs center service">Learn from one of the best teaching pros in the state, Dale Pemberton, with this<br>unique program which combines live lessons, structured practice, and<br>online check-ins to help keep you accountable for your progress.<br>You will also have access to a website with over <b>50 videos</b> and<br>counting to help you retain the information from the lessons.</p>
  <p class="abs center web"><span class="rule"></span>www.dale-pemberton.example<span class="rule"></span></p>
</section>

<section class="flyer back">
  <svg class="shapes" width="541" height="701" viewBox="0 0 541 701">
    <path fill="var(--brush)" d="M215,48 L262,42 L400,40 L520,46 L515,52 L500,56 L512,64 L490,70 L508,78 L470,84 L484,92 L440,98 L300,102 L230,100 L240,94 L212,88 L228,80 L210,72 L226,64 L208,58 Z"/>
    <polygon fill="var(--red)" points="272,116 385,295 159,295"/>
    <polygon fill="var(--tier-gray)" points="159,295 385,295 468,428 76,428"/>
    <polygon fill="var(--teal)" points="76,428 468,428 541,546 0,546"/>
    <line x1="272" y1="114" x2="210" y2="212" stroke="var(--ink)" stroke-width="1.6"/>
    <line x1="272" y1="114" x2="334" y2="212" stroke="var(--ink)" stroke-width="1.6"/>
    <line x1="0" y1="542" x2="50" y2="462" stroke="var(--ink)" stroke-width="1.6"/>
    <line x1="541" y1="542" x2="491" y2="462" stroke="var(--ink)" stroke-width="1.6"/>
    <rect x="0" y="546" width="541" height="68" fill="var(--white)"/>
    <rect x="0" y="614" width="541" height="87" fill="var(--red)"/>
  </svg>

  <span class="mark-dot"></span>
  <div class="wordmark">Dale<br>Pemberton<br>Golf</div>
  <h3 class="abs brush-title">GOLF LESSON MONTHLY<br>SUBSCRIPTIONS</h3>

  <div class="abs tier one" style="top:158px">
    <p class="name">TIER 1</p>
    <p class="lines">Lessons with Dale’s Assistant<br><em>$400 a month</em>, <em>$1100</em> for <em>3 months</em>,<br><em>$2100</em> for <em>6 months</em><br>Each month you get:<br><em>290 min</em> Lessons<br><em>245 min</em> practice sessions<br><em>45 min</em> short game lesson<br><em>4 online</em> checkins with Dale<br>+</p>
    <p class="pack"><em>3 month</em> package gets <em>1 playing</em> lesson,<br><em>6 month</em> package gets <em>3 playing</em> lessons</p>
  </div>

  <div class="abs tier two" style="top:299px">
    <p class="name">TIER 2</p>
    <p class="lines">Same as above but Lessons are with Dale<br><em>$600 a month, $1700</em> for <em>3 months, $3400</em> for <em>6 months</em><br>Each month you get:<br><em>290 min</em> Lessons<br><em>245 min</em> practice sessions<br><em>45 min</em> short game lesson<br><em>4 online</em> checkins with Dale<br>+</p>
    <p class="pack"><em>3 month</em> package gets <em>1 playing</em> lesson,<br><em>6 month</em> package gets <em>3 playing</em> lessons</p>
  </div>

  <div class="abs tier three" style="top:435px">
    <p class="name">TIER 3</p>
    <p class="lines"><em>$800 a month, $2300</em> for <em>3 months, $4500</em> for <em>6 months</em><br>Each month you get:<br><em>490 min</em> Lessons<br><em>445 min</em> practice sessions<br><em>4</em> Online Checkins<br>+</p>
    <p class="pack"><em>3 month</em> package gets <em>1 playing</em> lesson,<br><em>6 month</em> package gets <em>3 playing</em> lessons</p>
  </div>

  <p class="abs center payments">Payments for <span>3 month</span> or <span>6 month</span> packages can<br>be broken down into payments per month</p>

  <div class="abs contact">
    <p class="head">Contact</p>
    <p>To schedule or for other questions</p>
    <p><span class="label">Website:</span> dpgolf.example</p>
    <p><span class="label">Email at:</span> dpgolf@example.com</p>
    <p><span class="label">Call at:</span> 555-014-2297</p>
  </div>
  <span class="badge one"></span>
  <span class="badge two"></span>
  <span class="badge three"></span>
</section>

</body>
</html>
```